Stationary and Logo Design Project

We need a full corporate logo and stationary design for our company Lumvira7Q. Lumvira7Q specializes in creating custom adult sex toys using CAD and 3D Printing technologies as part of the process. The companies tagline is "Your Pleasure, Your Way", though this is not required to be part of the logo.

We are looking for something sensual, romantic and sexy, but not something explicit and vulgar.

As the company will be targeting mid to high-end clientele tastefulness is very important to us - this is difficult when the service we are selling is sex but can be achieved.

What we are after:

1. Logo
2. Business Card Design
3. Letterhead Design
4. Email Signature Design

File Formats we require in colour, greyscale and Black and White:

1 .AI
2 .EPS
3 .TIF
4 .PDF
5 .PNG (300 dpi)
6 .JPG (300 dpi)
7 .GIF (300 dpi)

Target Market(s)

Adults between the ages of 21 and 50 (Predominantly female but not limited to) who like there sex toys and want a custom job.

Industry/Entity Type

Adult

Requirements
Must have
• As we are planning on advertising in the future make sure the art is suitable for print advertising.
Nice to have
• The tagline "Your Pleasure, Your Way" on the business card, letterhead and email signature.
Should not have
• Explicit/vulgar illustrations.

"Clip-Art" should not be used.

```html
<!DOCTYPE html>
<html lang="en">
<head>
<meta charset="utf-8">
<title>Lumvira7Q Stationery</title>
<link rel="stylesheet" href="https://fonts.googleapis.com/css2?family=Gentium+Book+Plus&display=swap">
<style>
  :root {
    --paper: #ffffff;
    --ink-grey: #939598;
    --rule-grey: #8a8a8d;
    --shadow: rgba(0, 0, 0, 0.35);
    --text-font: "Gentium Book Plus", Georgia, serif;
  }
  html, body {
    margin: 0;
    padding: 0;
    width: 1200px;
    height: 1000px;
    overflow: hidden;
    background: var(--paper);
    font-family: var(--text-font);
    color: var(--ink-grey);
  }
  .canvas {
    position: relative;
    width: 1200px;
    height: 1000px;
  }
  .sheet {
    position: absolute;
    background: var(--paper);
    box-shadow: 6px 8px 14px var(--shadow);
  }
  .letterhead {
    left: 525px; top: 104px; width: 590px; height: 808px;
    outline: 1px solid #555;
  }
  .business-card {
    left: 462px; top: 348px; width: 514px; height: 302px;
  }
  .email-signature {
    left: 98px; top: 698px; width: 867px; height: 145px;
    border-radius: 46px;
  }
  .abs { position: absolute; margin: 0; white-space: nowrap; line-height: 1; }
  .brand-name { color: var(--ink-grey); font-weight: 400; letter-spacing: 0.5px; }
  .tagline { color: var(--ink-grey); }
  .divider { position: absolute; background: var(--rule-grey); }
  .mark { position: absolute; }

  /* letterhead */
  .letterhead .brand-name { left: 40px; top: 44px; font-size: 26px; }
  .letterhead .tagline { left: 43px; top: 75px; font-size: 14px; }
  .letterhead .divider { left: 255px; top: 31px; width: 2px; height: 68px; }
  .letterhead .contact-phone { left: 268px; top: 48px; font-size: 14px; }
  .letterhead .contact-email { left: 268px; top: 67px; font-size: 12px; }
  .letterhead .contact-web { left: 268px; top: 82px; font-size: 14px; }
  .letterhead .mark { left: 456px; top: 51px; }

  /* business card */
  .business-card .brand-name { left: 38px; top: 66px; font-size: 42px; }
  .business-card .tagline { left: 38px; top: 116px; font-size: 22px; }
  .business-card .divider { left: 38px; top: 166px; width: 440px; height: 2px; }
  .business-card .contact-phone { left: 49px; top: 197px; font-size: 21px; }
  .business-card .contact-email { left: 49px; top: 227px; font-size: 18px; }
  .business-card .contact-web { left: 49px; top: 249px; font-size: 20px; }
  .business-card .mark { left: 344px; top: 200px; }

  /* email signature */
  .email-signature .brand-name { left: 40px; top: 35px; font-size: 40px; }
  .email-signature .tagline { left: 45px; top: 84px; font-size: 20px; }
  .email-signature .divider { left: 375px; top: 14px; width: 2px; height: 103px; }
  .email-signature .contact-phone { left: 394px; top: 40px; font-size: 20px; }
  .email-signature .contact-email { left: 394px; top: 69px; font-size: 17px; }
  .email-signature .contact-web { left: 394px; top: 93px; font-size: 19px; }
  .email-signature .mark { left: 689px; top: 39px; }
</style>
</head>
<body>
<main class="canvas">

  <section class="sheet letterhead" aria-label="Letterhead">
    <p class="abs brand-name">Lumvira7Q</p>
    <p class="abs tagline">Your Pleasure, Your Way</p>
    <span class="divider"></span>
    <p class="abs contact-phone">ph 24461230897654</p>
    <p class="abs contact-email">Ada Whitlow@lumvira7q.com</p>
    <p class="abs contact-web">www.lumvira7q.com</p>
    <svg class="mark" width="94" height="48" viewBox="0 0 94 48" aria-hidden="true">
      <rect x="0" y="21" width="30" height="5" fill="var(--ink-grey)"/>
      <rect x="40" y="21" width="52" height="5" fill="var(--ink-grey)"/>
      <rect x="63" y="0" width="5" height="47" fill="var(--ink-grey)"/>
    </svg>
  </section>

  <section class="sheet business-card" aria-label="Business card">
    <p class="abs brand-name">Lumvira7Q</p>
    <p class="abs tagline">Your Pleasure, Your Way</p>
    <span class="divider"></span>
    <p class="abs contact-phone">ph 24461230897654</p>
    <p class="abs contact-email">Ada Whitlow@lumvira7q.com</p>
    <p class="abs contact-web">www.lumvira7q.com</p>
    <svg class="mark" width="144" height="82" viewBox="0 0 144 82" aria-hidden="true">
      <rect x="0" y="36" width="47" height="8" fill="var(--ink-grey)"/>
      <rect x="61" y="36" width="82" height="8" fill="var(--ink-grey)"/>
      <rect x="97" y="0" width="8" height="80" fill="var(--ink-grey)"/>
    </svg>
  </section>

  <section class="sheet email-signature" aria-label="Email signature">
    <p class="abs brand-name">Lumvira7Q</p>
    <p class="abs tagline">Your Pleasure, Your Way</p>
    <span class="divider"></span>
    <p class="abs contact-phone">ph 24461230897654</p>
    <p class="abs contact-email">Ada Whitlow@lumvira7q.com</p>
    <p class="abs contact-web">www.lumvira7q.com</p>
    <svg class="mark" width="144" height="80" viewBox="0 0 144 80" aria-hidden="true">
      <rect x="0" y="35" width="49" height="8" fill="var(--ink-grey)"/>
      <rect x="59" y="35" width="83" height="8" fill="var(--ink-grey)"/>
      <rect x="96" y="0" width="8" height="78" fill="var(--ink-grey)"/>
    </svg>
  </section>

</main>
</body>
</html>
```